Mental Health Awareness License Plates

Below is the sample format I will need. That of a plain license plate w/o frame
*refer to image with name Licence wo Frame*
Delete Frame
Replace QR Code with “MO”
Replace 2025 sticker with “ YR
Use License Plate font (attached)
On Ribbon, keep the green background
The California front leg, needs to be gradated like a sunset and retain shape of CA
Palm trees sharpened
I need the files in a format that can be used on a website, printed or made into a poster.
One file that reads SAMPLE, one version that reads “NEWPLA8”d
The finished product should look like a license plate as shown in the example
*refer to image name finished product*
I want to clarify what we are looking for. The license plate design has been approved by the state, but we need a high res version of it in multiple file formats. The most important change we are looking for is to the ribbon. The palm trees against the sunset are fuzzy, we need those placed in front of an sunset on the front leg of the ribbon. The rear leg needs to remain green (mental health color). I hope this help clarify our design need.

```html
<!DOCTYPE html>
<html lang="en">
<head>
<meta charset="utf-8">
<title>Mental Health Awareness License Plates</title>
<link rel="stylesheet" href="https://fonts.googleapis.com/css2?family=Barlow+Condensed:wght@500&family=Montserrat:wght@500;700&display=swap">
<style>
  :root {
    --page: #ffffff;
    --plate-mint: #c3e7e2;
    --plate-grey: #e4e5e7;
    --plate-edge: #f3f5f5;
    --ink: #0f1c24;
    --state-red: #e6394f;
    --ribbon-light: #ffb42a;
    --ribbon-deep: #f06a1c;
    --hole: #ffffff;
    --shadow: rgba(60, 70, 80, 0.28);
  }
  * { box-sizing: border-box; margin: 0; padding: 0; }
  html, body {
    width: 1200px;
    height: 1200px;
    overflow: hidden;
    background: var(--page);
  }
  .canvas {
    position: relative;
    width: 1200px;
    height: 1200px;
  }
  .plate {
    position: absolute;
    left: 203px;
    width: 783px;
    height: 383px;
    border-radius: 16px;
    box-shadow: 6px 10px 14px var(--shadow);
    overflow: hidden;
  }
  .plate--mint { top: 177px; background: var(--plate-mint); }
  .plate--grey { top: 617px; background: var(--plate-grey); }

  .plate__hole {
    position: absolute;
    width: 12px;
    height: 12px;
    border-radius: 50%;
    background: var(--hole);
    box-shadow: inset 0 0 0 1px rgba(0,0,0,0.08);
  }
  .plate__hole--tl { left: 129px; top: 5px; }
  .plate__hole--tr { left: 642px; top: 5px; }
  .plate__hole--bl { left: 129px; top: 352px; }
  .plate__hole--br { left: 642px; top: 352px; }

  .sticker-box {
    position: absolute;
    top: 40px;
    width: 115px;
    height: 61px;
    border: 2px solid var(--state-red);
    display: flex;
    align-items: center;
    justify-content: center;
    font-family: "Montserrat", sans-serif;
    font-weight: 500;
    font-size: 14px;
    letter-spacing: 1px;
    color: var(--state-red);
  }
  .sticker-box--month { left: 45px; }
  .sticker-box--year { left: 623px; }
  .sticker-box--year span {
    border-bottom: 2px solid var(--state-red);
    line-height: 1.2;
  }

  .state-name {
    position: absolute;
    left: 199px;
    top: 44px;
    width: 386px;
    height: 62px;
    border-radius: 30px;
    background: linear-gradient(90deg, rgba(230,57,79,0.75), rgba(230,57,79,0.55));
  }

  .ribbon {
    position: absolute;
    left: 37px;
    top: 129px;
    width: 121px;
    height: 205px;
  }

  .plate-number {
    position: absolute;
    left: 170px;
    top: 98px;
    width: 590px;
    text-align: center;
    font-family: "Barlow Condensed", sans-serif;
    font-weight: 500;
    font-size: 214px;
    line-height: 1;
    letter-spacing: 2px;
    color: var(--ink);
    text-shadow: 0 0 3px var(--plate-edge), 0 0 2px var(--plate-edge);
    white-space: nowrap;
  }

  .plate-tagline {
    position: absolute;
    left: 174px;
    top: 328px;
    width: 441px;
    font-family: "Montserrat", sans-serif;
    font-weight: 700;
    font-size: 24px;
    letter-spacing: 0.6px;
    color: var(--ink);
    white-space: nowrap;
  }
</style>
</head>
<body>
<main class="canvas">

  <section class="plate plate--mint" aria-label="License plate, mint version">
    <span class="plate__hole plate__hole--tl"></span>
    <span class="plate__hole plate__hole--tr"></span>
    <span class="plate__hole plate__hole--bl"></span>
    <span class="plate__hole plate__hole--br"></span>
    <div class="sticker-box sticker-box--month">MO</div>
    <div class="sticker-box sticker-box--year"><span>YR</span></div>
    <div class="state-name" role="img" aria-label="Script state name lettering: California"></div>
    <svg class="ribbon" viewBox="0 0 121 205" role="img" aria-label="Awareness ribbon illustration">
      <defs>
        <linearGradient id="ribbon-tone-a" x1="0" y1="0" x2="0" y2="1">
          <stop offset="0" stop-color="#ffb42a"/>
          <stop offset="1" stop-color="#f06a1c"/>
        </linearGradient>
      </defs>
      <rect x="8" y="0" width="105" height="205" rx="40" fill="url(#ribbon-tone-a)"/>
    </svg>
    <div class="plate-number">SAM 123</div>
    <div class="plate-tagline">MENTAL HEALTH AWARENESS</div>
  </section>

  <section class="plate plate--grey" aria-label="License plate, grey version">
    <span class="plate__hole plate__hole--tl"></span>
    <span class="plate__hole plate__hole--tr"></span>
    <span class="plate__hole plate__hole--bl"></span>
    <span class="plate__hole plate__hole--br"></span>
    <div class="sticker-box sticker-box--month">MO</div>
    <div class="sticker-box sticker-box--year"><span>YR</span></div>
    <div class="state-name" role="img" aria-label="Script state name lettering: California"></div>
    <svg class="ribbon" viewBox="0 0 121 205" role="img" aria-label="Awareness ribbon illustration">
      <defs>
        <linearGradient id="ribbon-tone-b" x1="0" y1="0" x2="0" y2="1">
          <stop offset="0" stop-color="#ffb42a"/>
          <stop offset="1" stop-color="#f06a1c"/>
        </linearGradient>
      </defs>
      <rect x="8" y="0" width="105" height="205" rx="40" fill="url(#ribbon-tone-b)"/>
    </svg>
    <div class="plate-number">SAM 123</div>
    <div class="plate-tagline">MENTAL HEALTH AWARENESS</div>
  </section>

</main>
</body>
</html>
```